Childcare Centre trifold brochure

Design a contemporary trifold brochure for a childcare centre that meets Australian printing requirements with supplied content, logo's, fonts and photo's. Please refer to the attached DL flyer front and back for similar possible style and content.

Target Market(s)

Families

Industry/Entity Type

Childcare

Requirements
Must have
• refer attached content, photo's, logo's and examples. Colours should be same as Pantone purple and green and or variations of. Refer attached dl flyer example.

```html
<!DOCTYPE html>
<html lang="en">
<head>
<meta charset="utf-8">
<title>Bright Sprouts – Trifold Brochure</title>
<link rel="stylesheet" href="https://fonts.googleapis.com/css2?family=Baloo+2:wght@600;800&family=Open+Sans:ital,wght@0,400;0,600;0,700;1,600&family=Gochi+Hand&display=swap">
<style>
  :root{
    --purple:#8b2b8e;
    --purple-dark:#6e1f72;
    --green:#2eaa47;
    --green-dark:#1f8b37;
    --paper:#ffffff;
    --ink:#4a4a4a;
    --stage:#e9e9ea;
    --photo-earth:#8a6a4a;
    --photo-leaf:#6f8a4a;
  }
  *{box-sizing:border-box;margin:0;padding:0}
  html,body{width:1200px;height:2400px;overflow:hidden;background:var(--stage)}
  body{font-family:"Open Sans",Arial,sans-serif;color:var(--ink);position:relative}

  .spread{position:absolute;left:50px;width:1100px;height:760px;display:grid;grid-template-columns:repeat(3,1fr);background:var(--paper);box-shadow:0 6px 24px rgba(0,0,0,.18)}
  .spread--outside{top:300px}
  .spread--inside{top:1340px}
  .panel{position:relative;overflow:hidden;height:760px}
  .panel + .panel{border-left:1px solid #e4e4e4}
  .curves{position:absolute;inset:0;width:100%;height:100%}

  .heading{font-family:"Baloo 2",Arial,sans-serif;font-weight:800;line-height:1}
  .heading .accent{color:var(--green)}
  .body-copy{font-size:10.5px;line-height:1.55}
  .body-copy p{margin-bottom:9px}

  .photo{position:absolute;background:linear-gradient(135deg,var(--photo-leaf),var(--photo-earth));}
  .photo--round{border-radius:50%}

  /* brand */
  .brand{display:flex;align-items:center;gap:10px}
  .brand__dot{width:30px;height:30px;border-radius:50%;background:var(--green);flex:none}
  .brand__name{font-family:"Baloo 2",Arial,sans-serif;font-weight:800;font-size:30px;color:var(--purple);line-height:1}
  .brand__tag{font-size:10.5px;color:var(--purple);font-weight:600;margin-top:2px}

  /* about panel */
  .about{background:var(--green);color:#fff;padding:30px 28px}
  .about .heading{font-size:30px;color:#fff;margin-bottom:18px}
  .about .lead{font-weight:700;font-style:italic}
  .about__footer{position:absolute;left:0;right:0;bottom:0;height:110px;background:var(--paper);padding:30px 28px}
  .about__footer .brand__name{font-size:24px}

  /* believe panel */
  .believe{padding:30px 28px}
  .believe .heading{font-size:30px;color:var(--purple);margin-bottom:12px}
  .quote{font-size:12px;font-weight:700;font-style:italic;color:var(--green-dark);line-height:1.5;margin-top:8px}
  .quote cite{display:block;text-align:right;font-weight:600;color:var(--purple);margin-top:4px}
  .hours{position:absolute;left:28px;right:24px;top:540px;color:#fff;font-size:10.5px;line-height:1.4}
  .hours__title{font-family:"Baloo 2",Arial,sans-serif;font-weight:800;font-size:20px}
  .hours__time{margin-bottom:12px}
  .hours__grid{display:grid;grid-template-columns:1fr 1fr;gap:0 12px}
  .hours__col{display:grid;gap:6px;align-content:start}
  .contact-line{display:flex;align-items:center;gap:6px}
  .contact-line--top{align-items:flex-start}
  .icon{width:14px;height:14px;flex:none}
  .social-line{position:absolute;left:28px;bottom:20px;color:#fff;font-weight:700;font-size:12px}
  .social-line__square{width:14px;height:14px;background:#fff;display:inline-block}
  .enrol-badge{position:absolute;width:80px;height:80px;border-radius:50%;background:var(--green);border:4px solid #fff;color:#fff;font-family:"Baloo 2",Arial,sans-serif;font-weight:800;font-size:16px;line-height:1;display:flex;align-items:center;justify-content:center;text-align:center}

  /* cover */
  .cover__brand{position:absolute;left:28px;top:30px}
  .award{position:absolute;border-radius:50%;background:var(--green);border:4px solid #fff;color:#fff;font-size:9px;font-weight:600;text-align:center;display:flex;flex-direction:column;align-items:center;justify-content:center;line-height:1.25;padding:8px}
  .award strong{font-size:12px;font-weight:700}
  .partner-badge{position:absolute;width:64px;height:64px;border-radius:50%;background:#fff;border:3px solid #ddd}
  .cover__title{position:absolute;left:40px;top:250px;width:290px;color:#fff;transform:rotate(-14deg);transform-origin:left top}
  .cover__title .heading{font-size:30px;letter-spacing:.5px}
  .cover__sub{font-size:12px;font-weight:700;color:#fff;margin-top:6px}
  .cover__years{font-family:"Baloo 2",Arial,sans-serif;font-weight:800;font-size:26px;color:#fff}
  .slogan{position:absolute;left:0;right:0;top:560px;text-align:center;font-family:"Gochi Hand",cursive;font-size:30px;color:#fff;line-height:1.1}
  .cover__contacts{position:absolute;left:28px;bottom:14px;color:#fff;font-weight:700;font-size:12px;display:grid;gap:4px}

  /* curriculum */
  .curriculum{padding:30px 28px}
  .curriculum .heading{font-size:28px;color:var(--purple);margin-bottom:12px}
  .highlight{color:var(--green-dark);font-weight:700;font-style:italic}
  .curriculum__web{position:absolute;left:0;right:0;bottom:22px;text-align:center;font-family:"Baloo 2",Arial,sans-serif;font-weight:800;font-size:24px;color:#fff}

  /* research */
  .enrol-band{position:absolute;left:0;right:0;top:0;padding:22px 24px 0 150px;color:#fff}
  .enrol-band .heading{font-size:19px}
  .enrol-band p{font-size:11px;font-style:italic;margin:4px 0 8px}
  .pill{display:inline-block;background:var(--purple);color:#fff;font-family:"Baloo 2",Arial,sans-serif;font-weight:800;font-size:15px;padding:4px 16px;border-radius:20px}
  .research{position:absolute;left:26px;right:24px;top:260px}
  .research .heading{font-size:22px;color:var(--purple);margin-bottom:12px}
  .research .heading .accent{display:block}
  .point-list{list-style:none;font-size:10.5px;line-height:1.5}
  .point-list li{display:flex;gap:9px;margin-bottom:11px}
  .point-list .marker{width:12px;height:12px;border-radius:50%;background:var(--purple);flex:none;margin-top:3px}

  /* activities */
  .activities{padding:240px 26px 0}
  .activities .heading{font-size:26px;color:var(--purple);margin-bottom:14px}
  .tick-list{list-style:none;font-size:10.5px;line-height:1.5}
  .tick-list li{display:flex;gap:10px;margin-bottom:12px}
  .tick-box{width:16px;height:16px;background:var(--green);flex:none;margin-top:2px;display:flex;align-items:center;justify-content:center}
  .garden{position:absolute;left:40px;right:40px;bottom:40px;height:110px;border-radius:12px;background:linear-gradient(180deg,#dff0d8,#9fcf7a)}
</style>
</head>
<body>

<section class="spread spread--outside" aria-label="Brochure outside">

  <article class="panel about">
    <h2 class="heading">About Us</h2>
    <div class="body-copy">
      <p class="lead">Providing outdoor opportunities for learning is a key priority for our team, and we share it with families and the wider community.</p>
      <p class="lead">Our outdoor learning was added to the national curriculum framework in 2018 and our educators support every child to explore it.</p>
      <p>Nature sparks passion, inspiration, creativity and growth. It plays an important role in the cognitive, emotional and physical development of children in their early years.</p>
      <p>Our centre has been a part of the local community for many years. We welcome children from six weeks to school age and offer long day care with a funded kindergarten program.</p>
      <p>Our open spaces let children climb, dig, build and discover at their own pace, guided by caring educators who know each child well.</p>
      <p>We believe the first years of a child's development are the most important, and we work with families to make them count.</p>
    </div>
    <footer class="about__footer">
      <div class="brand">
        <span class="brand__dot"></span>
        <div>
          <div class="brand__name">Bright Sprouts</div>
          <div class="brand__tag">Early Development &amp; Education Centre</div>
        </div>
      </div>
    </footer>
  </article>

  <article class="panel believe">
    <svg class="curves" viewBox="0 0 367 760" preserveAspectRatio="none" aria-hidden="true">
      <path d="M0 470 C120 430 240 520 367 470 L367 760 L0 760 Z" fill="var(--purple)"/>
      <path d="M0 700 L367 700 L367 760 L0 760 Z" fill="var(--green)"/>
    </svg>
    <h2 class="heading">We <span class="accent">Believe</span></h2>
    <div class="body-copy">
      <p>That the most wonderful things happen outdoors when children are given time and space to play, wonder and discover together with the natural world around them.</p>
    </div>
    <blockquote class="quote">“Passion is lifted from the earth itself by the muddy hands of the young; it travels along grass-stained sleeves to the heart. If we are going to save the environment, we must also save an endangered indicator species: the child in nature.”
      <cite>– Morgan Ellis</cite>
    </blockquote>
    <div class="photo photo--round" style="left:20px;top:330px;width:150px;height:150px" role="img" aria-label="Photo of a child in a sun hat playing outdoors"></div>
    <div class="photo photo--round" style="left:170px;top:370px;width:110px;height:110px" role="img" aria-label="Photo of the centre's garden play area"></div>
    <div class="enrol-badge" style="left:270px;top:420px">ENROL<br>NOW</div>
    <div class="hours">
      <div class="hours__title">Opening Hours:</div>
      <div class="hours__time">6:30am – 6:00pm Monday – Friday</div>
      <div class="hours__grid">
        <div class="hours__col">
          <div class="contact-line contact-line--top">
            <svg class="icon" viewBox="0 0 16 16"><path d="M8 1a5 5 0 0 0-5 5c0 4 5 9 5 9s5-5 5-9a5 5 0 0 0-5-5zm0 7a2 2 0 1 1 0-4 2 2 0 0 1 0 4z" fill="#fff"/></svg>
            <span>22 Wattle Street,<br>Greenhill Park</span>
          </div>
        </div>
        <div class="hours__col">
          <div class="contact-line">
            <svg class="icon" viewBox="0 0 16 16"><path d="M4 1l3 3-2 2c1 2 3 4 5 5l2-2 3 3-2 3C7 15 1 9 1 3z" fill="#fff"/></svg>
            <span>08 9000 1234</span>
          </div>
          <div class="contact-line">
            <svg class="icon" viewBox="0 0 16 16"><circle cx="8" cy="8" r="6.5" fill="none" stroke="#fff" stroke-width="1.5"/><path d="M1.5 8h13M8 1.5c-3 3-3 10 0 13M8 1.5c3 3 3 10 0 13" fill="none" stroke="#fff" stroke-width="1.2"/></svg>
            <span>brightsprouts.com.au</span>
          </div>
        </div>
      </div>
    </div>
    <div class="contact-line social-line">
      <span class="social-line__square"></span>
      <span>brightsproutsAU</span>
    </div>
  </article>

  <article class="panel cover">
    <svg class="curves" viewBox="0 0 367 760" preserveAspectRatio="none" aria-hidden="true">
      <path d="M0 520 C120 480 250 560 367 500 L367 760 L0 760 Z" fill="var(--purple)"/>
      <path d="M0 670 C140 650 260 690 367 660 L367 760 L0 760 Z" fill="var(--green)"/>
    </svg>
    <div class="cover__brand">
      <div class="brand">
        <span class="brand__dot"></span>
        <div>
          <div class="brand__name">Bright Sprouts</div>
          <div class="brand__tag">Early Development &amp; Education Centre</div>
        </div>
      </div>
    </div>
    <div class="photo photo--round" style="left:-10px;top:140px;width:380px;height:380px;border:7px solid var(--green)" role="img" aria-label="Photo of children playing among logs and trees in the outdoor play area"></div>
    <div class="cover__title">
      <div class="heading">GUIDING<br>THE STEWARDS<br>OF THE FUTURE</div>
      <div class="cover__sub">Finalist, Early Childhood Service of the Year</div>
      <div class="cover__years">2018, 2017 &amp; 2016</div>
    </div>
    <div class="award" style="right:12px;top:110px;width:98px;height:98px">Finalist<br>Early Childhood<br>Director of the Year<strong>2016</strong></div>
    <div class="award" style="right:18px;top:400px;width:96px;height:96px">WA State winner<br>Early Childhood<br>Educator of the Year<strong>2018</strong></div>
    <div class="partner-badge" style="left:70px;top:470px"></div>
    <div class="slogan">But of little things<br>big things grow</div>
    <div class="cover__contacts">
      <div class="contact-line"><svg class="icon" viewBox="0 0 16 16"><rect x="1" y="3" width="14" height="10" fill="#fff"/><path d="M1 3l7 6 7-6" fill="none" stroke="var(--green)" stroke-width="1.4"/></svg>hello@brightsprouts.com.au</div>
      <div class="contact-line"><svg class="icon" viewBox="0 0 16 16"><path d="M4 1l3 3-2 2c1 2 3 4 5 5l2-2 3 3-2 3C7 15 1 9 1 3z" fill="#fff"/></svg>08 9000 1234</div>
      <div class="contact-line"><svg class="icon" viewBox="0 0 16 16"><circle cx="8" cy="8" r="6.5" fill="none" stroke="#fff" stroke-width="1.5"/><path d="M1.5 8h13M8 1.5c-3 3-3 10 0 13M8 1.5c3 3 3 10 0 13" fill="none" stroke="#fff" stroke-width="1.2"/></svg>brightsprouts.com.au</div>
    </div>
  </article>
</section>

<section class="spread spread--inside" aria-label="Brochure inside">

  <article class="panel curriculum">
    <svg class="curves" viewBox="0 0 367 760" preserveAspectRatio="none" aria-hidden="true">
      <path d="M0 660 C120 620 250 700 367 650 L367 760 L0 760 Z" fill="var(--purple)"/>
    </svg>
    <h2 class="heading">Our <span class="accent">Curriculum</span></h2>
    <div class="body-copy">
      <p>We are a Reggio Emilia inspired childcare centre offering long day care and a funded kindergarten program for three to five year olds.</p>
      <p>At the core of our program is a child-first, emergent curriculum. Learning is shaped by each child's interests and delivered in a way that is meaningful to them.</p>
      <p class="highlight">Learning occurs naturally: children thrive and learn best when their interests are considered and explored.</p>
      <p>Much of our day is spent outdoors, where children develop a sense of adventure and connection with the environment, science, technology and maths.</p>
      <p>Our children spend their days among natural play spaces, a vegetable garden, a mud kitchen and quiet corners for rest, with chickens and a fire pit for shared stories.</p>
    </div>
    <div class="photo photo--round" style="left:70px;top:470px;width:180px;height:180px;border:6px solid var(--green)" role="img" aria-label="Photo of a child in a hat crouching and exploring the ground"></div>
    <div class="curriculum__web">brightsprouts.com.au</div>
  </article>

  <article class="panel">
    <svg class="curves" viewBox="0 0 367 760" preserveAspectRatio="none" aria-hidden="true">
      <path d="M0 0 L367 0 L367 190 C250 230 120 170 0 220 Z" fill="var(--green)"/>
    </svg>
    <div class="photo photo--round" style="left:16px;top:30px;width:120px;height:120px;border:5px solid #fff" role="img" aria-label="Photo of children building with blocks"></div>
    <div class="photo photo--round" style="left:120px;top:150px;width:76px;height:76px;border:4px solid #fff" role="img" aria-label="Photo of a mud kitchen"></div>
    <div class="enrol-band">
      <div class="heading">LOOKING TO ENROL YOUR CHILD?</div>
      <p>Become part of our wonderful family</p>
      <span class="pill">ENROL NOW</span>
    </div>
    <div class="research">
      <h2 class="heading">WHAT THE <span class="accent">RESEARCH SAYS</span></h2>
      <ul class="point-list">
        <li><span class="marker"></span><span>Outdoor play supports children's wellbeing, with studies showing improved concentration, calmer moods and stronger social skills.</span></li>
        <li><span class="marker"></span><span>Children's confidence grows when they take on healthy challenges, building resilience and independence.</span></li>
        <li><span class="marker"></span><span>Children who play regularly in natural settings are sick less often and show better motor fitness and coordination.</span></li>
        <li><span class="marker"></span><span>Children who spend more time outside are more physically active and more likely to keep healthy habits as adults.</span></li>
        <li><span class="marker"></span><span>Play in nature is more diverse and imaginative, encouraging language, creativity and collaboration with peers.</span></li>
      </ul>
    </div>
  </article>

  <article class="panel activities">
    <svg class="curves" viewBox="0 0 367 760" preserveAspectRatio="none" aria-hidden="true">
      <path d="M0 0 L367 0 L367 150 C260 200 130 120 0 170 Z" fill="var(--green)"/>
    </svg>
    <div class="photo photo--round" style="left:170px;top:24px;width:110px;height:110px;border:5px solid #fff" role="img" aria-label="Photo of the outdoor sandpit and trees"></div>
    <h2 class="heading" style="position:relative">Our <span class="accent">Activities</span></h2>
    <ul class="tick-list" style="position:relative">
      <li><span class="tick-box"><svg width="10" height="10" viewBox="0 0 10 10"><path d="M1 5l3 3 5-6" fill="none" stroke="#fff" stroke-width="1.8"/></svg></span><span>Children are taught real-life skills such as planting, cooking and caring for animals, supported by educators through hands-on experiences every day.</span></li>
      <li><span class="tick-box"><svg width="10" height="10" viewBox="0 0 10 10"><path d="M1 5l3 3 5-6" fill="none" stroke="#fff" stroke-width="1.8"/></svg></span><span>The significant importance of learning through play is recognised and a natural environment is central to our program.</span></li>
      <li><span class="tick-box"><svg width="10" height="10" viewBox="0 0 10 10"><path d="M1 5l3 3 5-6" fill="none" stroke="#fff" stroke-width="1.8"/></svg></span><span>Just as importantly, our children are able to explore and play at their own pace and share their discoveries.</span></li>
    </ul>
    <div class="garden" role="img" aria-label="Illustration of trees and a child playing on grass"></div>
  </article>
</section>

</body>
</html>
```